Health & Fitness Retreat Homepage Design

We have an existing website at http://www.BluePineHavens.com.au which we are retaining but wish to have a freshly designed homepage with the existing top navigation bar.
Sample layout is attached, but feel free to use your creativity on layout and colours, always remembering it needs to fit with the wider site design.
Project Delivery:
5 phase slide slow at top of homepage
Full homepage design and associated files
Target Audience:
- Female 80%, Male 20%
- Aged 30 to 50
- Overweight/Obese (so no pictures of thin people)
See attached layout for more information.
Target Market(s)
Target Audience:
- Female 80%, Male 20%
- Aged 30 to 50
Industry/Entity Type
Fitness
Requirements
Must have
- Must have existing top navigation bar as at http://www.BluePineHavens.com.au and fit with existing interior colours, etc.
Should not have
- No pictures of thin people

```html
<!DOCTYPE html>
<html lang="en">
<head>
<meta charset="utf-8">
<title>BluePine Havens – Weight Loss Retreat</title>
<link href="https://fonts.googleapis.com/css2?family=Bebas+Neue&family=Jost:wght@400;500;600&display=swap" rel="stylesheet">
<style>
:root{
  --frame:#e4e5e6;
  --band:#6f8899;
  --orange:#f08a1c;
  --orange-dark:#e2621b;
  --blue:#1ba9e1;
  --green:#5bb431;
  --slate:#555a5e;
  --ink:#222;
  --white:#fff;
}
*{box-sizing:border-box;margin:0;padding:0}
html,body{width:847px;height:1200px;overflow:hidden;background:#fff;font-family:"Jost",sans-serif;color:var(--ink)}
.canvas{position:relative;width:847px;height:1200px}
.abs{position:absolute}
.frame{left:17px;top:21px;width:815px;height:1155px;border-radius:20px;background:var(--frame)}
.page{left:31px;top:38px;width:786px;height:1124px;background:linear-gradient(#f3f3f3,#fff 40%,#fafafa)}
.hero-band{left:31px;top:38px;width:786px;height:436px;background:var(--band)}
.header{left:105px;top:38px;width:636px;height:99px;background:var(--white);border-radius:0 0 14px 14px}
.brand{left:135px;top:70px;display:flex;align-items:center;gap:6px;font-weight:600;font-size:18px;color:var(--orange);letter-spacing:.3px;white-space:nowrap}
.brand .dot{width:18px;height:18px;border-radius:50%;background:var(--green)}
.navcol{top:57px;font-size:6px;line-height:11px;color:#333}
.navcol h4{font-size:7px;font-weight:600;border-bottom:1px solid #999;margin-bottom:3px;letter-spacing:.3px;line-height:9px}
.navcol li{list-style:none}
.navcol li::before{content:"› ";font-weight:600}
.promo{left:657px;top:56px;width:59px;height:31px;background:linear-gradient(90deg,#c9b8a5,#d8413a)}
.brochure{left:657px;top:94px;width:59px;height:20px;border-radius:3px;background:var(--orange);color:#fff;font-size:6.5px;font-weight:600;text-align:center;line-height:20px;letter-spacing:.5px}
.slider{left:105px;top:127px;width:634px;height:308px;background:var(--slate);border-radius:14px}
.slide{left:125px;top:146px;width:600px;height:278px;background:var(--white);border-radius:12px}
.hero-photo{left:165px;top:150px;width:263px;height:274px;background:radial-gradient(ellipse at 50% 40%,#e9b79a,#d5502d 55%,#fff 80%)}
.kicker{left:438px;top:199px;font-family:"Bebas Neue",sans-serif;font-size:12px;letter-spacing:2px;color:var(--green)}
.headline{left:436px;top:208px;font-family:"Bebas Neue",sans-serif;font-size:49px;letter-spacing:2px;color:var(--orange);line-height:48px}
.sub{left:438px;top:251px;font-size:7px;letter-spacing:1.4px;font-weight:500;color:#444;text-transform:uppercase}
.sub b{color:var(--orange)}
.points{left:438px;top:271px;list-style:none;font-size:7px;letter-spacing:1.3px;color:#444;text-transform:uppercase}
.points li{display:flex;align-items:center;gap:8px;height:18px}
.points svg{width:8px;height:8px}
.btn-learn{left:578px;top:327px;width:84px;height:21px;border-radius:4px;background:var(--orange);color:#fff;font-family:"Bebas Neue",sans-serif;font-size:12px;letter-spacing:1.5px;text-align:center;line-height:22px}
.dots{left:578px;top:401px;display:flex;gap:5px}
.dots span{width:12px;height:12px;border-radius:50%;background:#f3b87a;border:2px solid #fbe3c8}
.dots span.on{background:#333;border-color:#bbb}
.tab{top:443px;width:152px;height:56px;color:#fff;font-family:"Bebas Neue",sans-serif;font-size:20px;letter-spacing:2px;line-height:20px;padding:9px 0 0 9px}
.tab svg{position:absolute;right:8px;top:19px;width:14px;height:18px}
.tab-orange{left:108px;background:linear-gradient(var(--orange),var(--orange-dark))}
.tab-blue{left:268px;background:linear-gradient(#2dc0f0,#139cd8)}
.tab-green{left:427px;background:linear-gradient(#6cc53d,#45a02a)}
.tab-dark{left:587px;background:linear-gradient(#555,#2a2a2a)}
.rule{left:86px;width:676px;height:1px;background:#e2e2e2}
.card{top:548px;height:217px;background:linear-gradient(#fff,#f1f1f1);box-shadow:0 1px 4px rgba(0,0,0,.25)}
.card .photo{position:absolute;left:9px;top:9px;right:9px;height:117px}
.card h3{position:absolute;left:9px;top:134px;font-size:9px;font-weight:600;letter-spacing:.8px;text-transform:uppercase}
.card p{position:absolute;left:9px;top:148px;right:9px;font-size:6.5px;line-height:11px;color:#444}
.card .more{position:absolute;right:9px;top:193px;width:59px;height:17px;border-radius:2px;color:#fff;font-size:6.5px;text-align:center;line-height:17px}
.card-a{left:111px;width:181px}
.card-b{left:339px;width:178px}
.card-c{left:558px;width:178px}
.badge{position:absolute;left:19px;top:15px;width:38px;height:38px;border-radius:50%;background:var(--orange)}
.section-title{left:113px;top:829px;font-size:9px;font-weight:500;letter-spacing:1.3px;color:var(--orange)}
.video{left:114px;top:851px;width:307px;height:154px;background:linear-gradient(90deg,#5a4a3a,#7a4a34 50%,#3a2c24);box-shadow:0 1px 4px rgba(0,0,0,.3)}
.play{left:196px;top:906px;width:44px;height:44px;background:rgba(120,120,120,.6);border:1px solid #ccc}
.bubble{top:857px;width:140px;height:68px;border-radius:6px;color:#fff;font-size:6.5px;line-height:11px;letter-spacing:.6px;padding:8px 10px}
.bubble::after{content:"";position:absolute;left:14px;bottom:-7px;border:7px solid transparent;border-bottom:0;border-top-color:inherit}
.bubble-orange{left:442px;background:var(--orange);border-color:var(--orange)}
.bubble-blue{left:597px;background:var(--blue);border-color:var(--blue)}
.avatar{top:934px;width:40px;height:40px}
.who{top:938px;font-size:8px;line-height:9px;letter-spacing:.4px}
.who small{display:block;font-size:6px;margin-top:6px;color:#444}
.view-more{left:662px;top:999px;font-size:6px;color:var(--orange);text-decoration:underline}
.fcol{top:1062px;font-size:5.5px;line-height:10px;color:#444}
.fcol h4{font-size:6.5px;font-weight:600;border-bottom:1px solid var(--orange);margin-bottom:2px;letter-spacing:.5px;line-height:9px;display:inline-block}
.fcol li{list-style:none}
.fcol li::before{content:"› ";font-weight:600}
.field{left:599px;width:122px;height:12px;border:1px solid #ccc;background:#fff;font-size:5px;line-height:10px;padding-left:3px;color:#555}
.subscribe{left:662px;top:1106px;width:59px;height:11px;background:linear-gradient(#666,#333);color:#fff;font-size:5px;text-align:center;line-height:11px;letter-spacing:1px}
.copyright{left:31px;top:1147px;width:786px;text-align:center;font-size:5px;color:#999;letter-spacing:.3px}
</style>
</head>
<body>
<div class="canvas">
  <div class="abs frame"></div>
  <div class="abs page"></div>
  <div class="abs hero-band"></div>

  <div class="abs header"></div>
  <div class="abs brand"><span class="dot"></span>BluePine Havens</div>
  <ul class="abs navcol" style="left:336px"><h4>THE BEST PROGRAMS</h4><li>Weight Loss Retreats</li><li>Fitness Camps</li><li>Health Retreats @ Home</li></ul>
  <ul class="abs navcol" style="left:442px"><h4>THE BEST LOCATIONS</h4><li>Blue Mountains, NSW</li><li>Central Coast, NSW</li><li>Victoria Retreats</li></ul>
  <ul class="abs navcol" style="left:556px"><h4>ABOUT BLUEPINE</h4><li>Why choose BluePine</li><li>What clients say...</li><li>Contact us</li><li>FREE Brochure</li><li>Special Offers</li></ul>
  <div class="abs promo" role="img" aria-label="Free brochure magazine cover with request now tag"></div>
  <div class="abs brochure">FREE Brochure</div>

  <div class="abs slider"></div>
  <div class="abs slide"></div>
  <div class="abs hero-photo" role="img" aria-label="Smiling curvy woman with red hair in a red dress, hands on hips"></div>
  <div class="abs kicker">TRANSFORM YOUR</div>
  <div class="abs headline">BODY &amp; LIFE</div>
  <div class="abs sub">At Australia's <b>No.1</b> weight loss &amp; fitness retreat</div>
  <ul class="abs points">
    <li><svg viewBox="0 0 8 8"><path d="M1 4.2l2 2 4-4.4" fill="none" stroke="#f08a1c" stroke-width="1.6"/></svg>For all shapes, sizes &amp; fitness levels</li>
    <li><svg viewBox="0 0 8 8"><path d="M1 4.2l2 2 4-4.4" fill="none" stroke="#f08a1c" stroke-width="1.6"/></svg>Stunning locations &amp; 1st class facilities</li>
    <li><svg viewBox="0 0 8 8"><path d="M1 4.2l2 2 4-4.4" fill="none" stroke="#f08a1c" stroke-width="1.6"/></svg>Amazing weight loss results</li>
  </ul>
  <div class="abs btn-learn">LEARN MORE</div>
  <div class="abs dots"><span class="on"></span><span></span><span></span><span></span><span></span></div>

  <div class="abs tab tab-orange">WEIGHT LOSS<br>RETREATS<svg viewBox="0 0 14 18"><path d="M1 1l6 8-6 8M7 1l6 8-6 8" fill="none" stroke="#c33a12" stroke-width="2.5"/></svg></div>
  <div class="abs tab tab-blue">FITNESS CAMPS<br>&amp; HOLIDAYS<svg viewBox="0 0 14 18"><path d="M1 1l6 8-6 8M7 1l6 8-6 8" fill="none" stroke="#0d6fb0" stroke-width="2.5"/></svg></div>
  <div class="abs tab tab-green">HOME WEIGHT<br>LOSS PROGRAM<svg viewBox="0 0 14 18"><path d="M1 1l6 8-6 8M7 1l6 8-6 8" fill="none" stroke="#2e7a18" stroke-width="2.5"/></svg></div>
  <div class="abs tab tab-dark">WEIGHT LOSS<br>OFFERS<svg viewBox="0 0 14 18"><path d="M1 1l6 8-6 8M7 1l6 8-6 8" fill="none" stroke="#111" stroke-width="2.5"/></svg></div>

  <div class="abs rule" style="top:525px"></div>

  <div class="abs card card-a">
    <div class="photo" role="img" aria-label="Retreat pool surrounded by bushland and mountain views" style="background:linear-gradient(#7fa35a,#3d6a38 55%,#37a9c0)"></div>
    <div class="badge"></div>
    <h3 style="color:var(--orange)">Blue Mountains, NSW</h3>
    <p>You will lose weight fast at the Blue Mountains Weight Loss Camp near Sydney. Stunning mountains scenery and 1st class facilities......</p>
    <div class="more" style="background:var(--orange)">read more ›</div>
  </div>
  <div class="abs card card-b">
    <div class="photo" role="img" aria-label="Resort pool at dusk beside the water" style="background:linear-gradient(#3a6fb0,#4d7aa0 50%,#2a9ac4)"></div>
    <h3 style="color:var(--blue)">Central Coast, NSW</h3>
    <p>Just 90 mins from Sydney our Central Coast NSW Weight Loss Retreats offers direct beach access and a 5 star resort style environm......</p>
    <div class="more" style="background:var(--blue)">read more ›</div>
  </div>
  <div class="abs card card-c">
    <div class="photo" role="img" aria-label="Resort villa with gardens and a bright pool" style="background:linear-gradient(#5aa9e0,#3e8a3a 50%,#2fc2d8)"></div>
    <h3 style="color:var(--green)">Victoria Retreats</h3>
    <p>Combine the luxury of the Seabrook Sands Resort in Torquay Victoria with the most most popular weight loss retreat prog......</p>
    <div class="more" style="background:var(--green)">read more ›</div>
  </div>

  <div class="abs rule" style="top:806px"></div>
  <div class="abs section-title">VIEW OUR WEIGHT LOSS RETREAT TESTIMONIAL VIDEOS</div>
  <div class="abs video" role="img" aria-label="Testimonial video still of a smiling woman"></div>
  <svg class="abs play" viewBox="0 0 44 44"><path d="M16 12l16 10-16 10z" fill="#eee"/></svg>

  <div class="abs bubble bubble-orange">"The BluePine Home Weight loss program has trained my mind to not want rubbish... the program diary has reconditioned the way I think about food."</div>
  <div class="abs bubble bubble-blue">"It is a sensational feeling when I meet people I haven't seen for a while and they realise that I lost over 7st."</div>
  <div class="abs avatar" role="img" aria-label="Portrait of Megan" style="left:442px;background:linear-gradient(#6a3a2a,#e0b9a0)"></div>
  <div class="abs who" style="left:488px">Megan from<br>Sydney<small>lost 4st 2lb</small></div>
  <div class="abs avatar" role="img" aria-label="Portrait of Doug" style="left:600px;width:36px;background:linear-gradient(#ddd,#d7a58a)"></div>
  <div class="abs who" style="left:643px">Doug from<br>Melbourne<small>lost 7st 10lb</small></div>
  <div class="abs view-more">View more testimonials</div>

  <div class="abs rule" style="top:1041px"></div>
  <ul class="abs fcol" style="left:119px"><h4>THE BEST PROGRAMS</h4><li>Weight Loss Retreats</li><li>Fitness Camps</li><li>Health Retreats @ Home</li></ul>
  <ul class="abs fcol" style="left:237px"><h4>THE BEST LOCATIONS</h4><li>Blue Mountains, NSW</li><li>Central Coast, NSW</li><li>Victoria Retreats</li></ul>
  <ul class="abs fcol" style="left:358px"><h4>ABOUT BLUEPINE</h4><li>Why choose BluePine</li><li>What clients say...</li><li>Book Now</li></ul>
  <ul class="abs fcol" style="left:471px"><h4>FREE INFORMATION</h4><li>Request a brochure</li><li>Free BluePine Magazine</li></ul>
  <div class="abs fcol" style="left:599px"><h4 style="border:0">SUBSCRIBE TO OUR NEWSLETTER</h4></div>
  <div class="abs field" style="top:1076px">Name:</div>
  <div class="abs field" style="top:1093px">Email:</div>
  <div class="abs subscribe">SUBSCRIBE</div>

  <div class="abs rule" style="top:1139px;left:230px;width:390px"></div>
  <div class="abs copyright">© 2012 BluePine Wellbeing PTY Ltd | ABN 00 000 000 000 | Special Offers | Book Now | Contact Us | Health Retreats | Home Weight Loss Program</div>
</div>
</body>
</html>
```